Two documents one design language.

We are a small insurance broker who is committed to being open and transparent as possible with our customers.

For years, we have used plain word documents (see attachments) for our Policy Wording and our Terms of Business.

But now think we can do better and these plain documents are falling behind what our competitors are offering.

So we are now looking for both these documents to be professionally designed using the same design language for both.

We are putting few constraints on the design, but we do have some:
- It must be done in word as the wording can be changed at any time, so we must be able to maintain the documents ourselves.
- Any pictures or graphics you use must be royalty free so we can re-produce with any complications.
- Any pictures or graphics you use must been supplied as part of the package.
- You MUST NOT change any wording or grammar, it's not ours to change, its the insurers wording and HAS to be agreed with them.
- You must not split any any paragraph or bullet point over two pages.
- We are an insurance broker so what ever design you use, must look professional and inspire confidence... I.e. if you read it your thoughts turn to, these people are approachable, know what they are doing and will look after me.
- We specialise in musical instrument insurance, so we are looking for musical theming.

```html
<!DOCTYPE html>
<html lang="en">
<head>
<meta charset="utf-8">
<title>Policy Wording – Calder Rowe Insurance Services</title>
<link rel="stylesheet" href="https://fonts.googleapis.com/css2?family=Lexend:wght@400;500;600&family=Quicksand:wght@500;600&display=swap">
<style>
  :root {
    --pink: #e06b8d;
    --pink-soft: #f3c4d2;
    --dark: #3a3636;
    --ink: #2b2b2b;
    --paper: #ffffff;
    --mist: #f1f1f2;
    --grey-note: #d9d9dc;
    --canvas: #ffffff;
  }
  * { box-sizing: border-box; margin: 0; padding: 0; }
  html, body { width: 1200px; height: 532px; overflow: hidden; background: var(--canvas); }
  .spread { position: relative; width: 1200px; height: 532px; }
  .page {
    position: absolute; top: 32px; width: 362px; height: 468px; overflow: hidden;
    background: linear-gradient(135deg, var(--mist) 0%, var(--paper) 45%, var(--mist) 100%);
    box-shadow: 0 1px 4px rgba(0,0,0,.12);
    font-family: "Quicksand", sans-serif; color: var(--ink);
  }
  .page > * { z-index: 2; }
  .page--cover { left: 32px; }
  .page--contents { left: 419px; }
  .page--info { left: 806px; background: var(--paper); }
  .frame { position: absolute; inset: 0; width: 362px; height: 468px; z-index: 1; }
  .heading { font-family: "Lexend", sans-serif; font-weight: 500; letter-spacing: -0.3px; }

  /* faint music watermarks */
  .music-watermark { position: absolute; z-index: 0; pointer-events: none; }
  .watermark-clef {
    left: 14px; top: 290px; width: 80px; height: 150px;
    background: radial-gradient(ellipse at 45% 50%, rgba(190,190,195,.35) 0%, rgba(255,255,255,0) 70%);
  }
  .watermark-staff-cover {
    left: 60px; top: 360px; width: 300px; height: 70px;
    background: linear-gradient(170deg, rgba(255,255,255,0) 20%, rgba(243,196,210,.35) 50%, rgba(255,255,255,0) 80%);
  }
  .watermark-staff-contents {
    left: 180px; top: 110px; width: 182px; height: 290px;
    background: linear-gradient(120deg, rgba(255,255,255,0) 30%, rgba(243,196,210,.3) 50%, rgba(255,255,255,0) 70%);
  }
  .watermark-notes-info {
    left: 300px; top: 300px; width: 62px; height: 150px;
    background: radial-gradient(ellipse at 60% 50%, rgba(243,196,210,.45) 0%, rgba(255,255,255,0) 70%);
  }

  /* cover */
  .hero-art {
    position: absolute; left: 70px; top: 40px; width: 226px; height: 306px; z-index: 1;
    background: radial-gradient(ellipse at 50% 45%, var(--pink-soft) 0%, #fbe7ee 55%, rgba(255,255,255,0) 75%);
  }
  .brand {
    position: absolute; left: 17px; top: 30px; z-index: 3; display: flex; align-items: center; gap: 6px;
    font-family: "Lexend", sans-serif; font-weight: 500; font-size: 11px; line-height: 13px; color: var(--dark);
    white-space: nowrap;
  }
  .brand-dot { width: 10px; height: 10px; border-radius: 50%; background: var(--pink); flex: none; }
  .tagline {
    position: absolute; left: 20px; right: 20px; top: 374px; text-align: center;
    font-size: 14.5px; line-height: 24px; color: var(--ink);
  }
  .tagline em { font-style: normal; color: var(--pink); }

  /* contents */
  .contents-title { position: absolute; left: 17px; top: 20px; font-size: 15px; color: var(--pink); }
  .toc { position: absolute; left: 34px; top: 45px; width: 296px; list-style: none; }
  .toc li {
    display: flex; justify-content: space-between; align-items: flex-start;
    font-family: "Lexend", sans-serif; font-weight: 500; font-size: 8.6px; line-height: 16px;
    margin-bottom: 5.8px; letter-spacing: -0.2px;
  }
  .toc .entry { width: 225px; }

  /* information */
  .info-title { position: absolute; left: 16px; top: 22px; font-size: 15px; font-weight: 600; color: var(--pink); }
  .info-text { font-size: 7px; line-height: 13.9px; text-align: justify; position: absolute; }
  .col-left { left: 14px; top: 52px; width: 157px; }
  .col-right { left: 199px; top: 52px; width: 137px; }
  .notice { left: 14px; top: 145px; width: 322px; color: var(--pink); }
  .notice b { font-weight: 500; color: var(--ink); }
  .ticks { position: absolute; list-style: none; }
  .ticks li { position: relative; padding-left: 20px; font-size: 7px; line-height: 13.9px; text-align: justify; }
  .ticks li svg { position: absolute; left: 4px; top: 3px; width: 7px; height: 7px; }
  .ticks-a { left: 14px; top: 180px; width: 146px; }
  .ticks-b { left: 191px; top: 180px; width: 145px; }
  .ticks-c { left: 14px; top: 273px; width: 146px; }
  .ticks-d { left: 191px; top: 273px; width: 145px; }
  .write-title {
    position: absolute; left: 14px; width: 322px; top: 359px; text-align: center;
    font-size: 8px; color: var(--pink); letter-spacing: -0.2px;
  }
  .ticks-e { left: 14px; top: 380px; width: 104px; }
  .ticks-f { left: 131px; top: 380px; width: 104px; }
  .ticks-g { left: 248px; top: 380px; width: 104px; }
</style>
</head>
<body>
<svg width="0" height="0" style="position:absolute">
  <defs>
    <symbol id="tick" viewBox="0 0 10 10">
      <circle cx="5" cy="5" r="4.2" fill="none" stroke="#e06b8d" stroke-width="1.4"/>
      <path d="M3 5.2 L4.5 6.6 L7.2 3.6" fill="none" stroke="#e06b8d" stroke-width="1.4"/>
    </symbol>
    <g id="page-frame">
      <path d="M243 0 H362 V120 L348 110 V13 H254 Z" fill="#e06b8d"/>
      <path d="M0 226 L14 236 V248 L0 238 Z" fill="#e06b8d"/>
      <path d="M0 244 L14 256 V264 L0 254 Z" fill="#3a3636"/>
      <path d="M0 264 L14 276 V454 H232 L246 468 H0 Z" fill="#3a3636"/>
      <path d="M238 454 H248 L262 468 H252 Z" fill="#3a3636"/>
      <path d="M254 454 H262 L276 468 H268 Z" fill="#3a3636"/>
      <path d="M268 454 H362 V468 H282 Z" fill="#e06b8d"/>
      <path d="M14 434 H150 L170 454 H14 Z" fill="#e4e4e6"/>
    </g>
  </defs>
</svg>

<main class="spread">
  <section class="page page--cover">
    <div class="music-watermark watermark-clef" role="img" aria-label="Faint grey treble clef watermark"></div>
    <div class="music-watermark watermark-staff-cover" role="img" aria-label="Faint pink music staff with notes sweeping across the page"></div>
    <svg class="frame" viewBox="0 0 362 468"><use href="#page-frame"/></svg>
    <div class="hero-art" role="img" aria-label="Pink line illustration of a winged cherub playing a harp"></div>
    <div class="brand"><span class="brand-dot"></span><span>CALDER ROWE<br>INSURANCE SERVICES</span></div>
    <p class="tagline heading">PROTECTING <em>THE INSTRUMENTS</em> THAT MAKE<br>THE MUSIC POSSIBLE.</p>
  </section>

  <section class="page page--contents">
    <div class="music-watermark watermark-staff-contents" role="img" aria-label="Faint pink music staff with notes rising diagonally"></div>
    <svg class="frame" viewBox="0 0 362 468"><use href="#page-frame"/></svg>
    <h2 class="contents-title heading">CONTENTS</h2>
    <ol class="toc">
      <li><span class="entry">DEFINITIONS</span><span>2</span></li>
      <li><span class="entry">POLICY OVERVIEW</span><span>3</span></li>
      <li><span class="entry">CERTIFICATE OF INSURANCE (PUBLIC LIABILITY)</span><span>4</span></li>
      <li><span class="entry">CERTIFICATE OF INSURANCE (MUSICAL INSTRUMENTS AND ACCESSORIES)</span><span>6</span></li>
      <li><span class="entry">SCHEDULE</span><span>8</span></li>
      <li><span class="entry">INFORMATION YOU HAVE GIVEN US</span><span>9</span></li>
      <li><span class="entry">YOUR DUTIES</span><span>10</span></li>
      <li><span class="entry">THE COVER PROVIDED</span><span>11</span></li>
      <li><span class="entry">PUBLIC LIABILITY COVER</span><span>13</span></li>
      <li><span class="entry">EXCLUSIONS</span><span>15</span></li>
      <li><span class="entry">HOW TO AMEND YOUR POLICY</span><span>23</span></li>
      <li><span class="entry">RENEWING YOUR POLICY</span><span>23</span></li>
      <li><span class="entry">HOW TO CANCEL YOUR POLICY</span><span>24</span></li>
      <li><span class="entry">CLAIMS CONDITIONS</span><span>26</span></li>
      <li><span class="entry">HOW TO MAKE A COMPLIANT</span><span>29</span></li>
      <li><span class="entry">AUTHORISATION &amp; REGULATION</span><span>32</span></li>
      <li><span class="entry">PRIVACY NOTICES</span><span>33</span></li>
    </ol>
  </section>

  <section class="page page--info">
    <div class="music-watermark watermark-notes-info" role="img" aria-label="Faint pink music notes along the right edge"></div>
    <svg class="frame" viewBox="0 0 362 468"><use href="#page-frame"/></svg>
    <h2 class="info-title heading">INFORMATION YOU HAVE GIVEN US</h2>
    <p class="info-text col-left">In deciding to accept this insurance and in setting the terms and premium, WE have relied on the information YOU have given US. YOU must take care when answering any questions WE ask by ensuring that all information provided is accurate and complete.</p>
    <p class="info-text col-right">If WE establish that YOU deliberately or recklessly provided US with false or misleading information WE will treat this insurance as if it never existed and decline all claims.</p>
    <p class="info-text notice">If <b>WE</b> establish that <b>YOU</b> carelessly provided <b>US</b> with false or misleading information it could adversely affect <b>YOUR</b> insurance and any claim.&nbsp; For example <b>WE</b> may:</p>

    <ul class="ticks ticks-a"><li><svg><use href="#tick"/></svg>treat this insurance as if it had never existed and refuse to pay all claims and return the premium paid. WE will only do this if WE provided YOU with insurance cover which WE would not otherwise have offered; or</li></ul>
    <ul class="ticks ticks-b"><li><svg><use href="#tick"/></svg>amend the terms of YOUR insurance. WE may apply these amended terms as if they were already in place if a claim has been adversely impacted by YOUR carelessness; or</li></ul>
    <ul class="ticks ticks-c"><li><svg><use href="#tick"/></svg>charge YOU more for YOUR insurance or reduce the amount WE pay on a claim in the proportion the premium YOU have paid bears to the premium WE would have charged YOU; or</li></ul>
    <ul class="ticks ticks-d"><li><svg><use href="#tick"/></svg>cancel YOUR insurance in accordance with the HOW TO CANCEL THIS POLICY section within this policy document.</li></ul>

    <h3 class="write-title heading">WE OR CALDER ROWE INSURANCE SERVICES WILL WRITE TO YOU IF WE:</h3>
    <ul class="ticks ticks-e"><li><svg><use href="#tick"/></svg>Intend to treat this insurance as if it never existed; or</li></ul>
    <ul class="ticks ticks-f"><li><svg><use href="#tick"/></svg>Need to amend the terms of YOUR insurance; or</li></ul>
    <ul class="ticks ticks-g"><li><svg><use href="#tick"/></svg>Require YOU to pay more for YOUR insurance.</li></ul>
  </section>
</main>
</body>
</html>
```